TORVEL Industrial Maintenance

I offer repair and maintenance services of industrial mechanics in Quebec. I would like a creation that reflects confidence, competence, professionalism and dynamism. I like the orange color and the blue color.

Target Market(s)

Industries and Manufacturing companies using industrial machinery for the manufacture of their products.

Industry/Entity Type

Manufacturing

Contact Information for Business Card

TORVEL Maintenance Industrielle
Tél: (450)-318-5947
Courriel: torvel.mnt@boitemel-exemple.com

Font styles to use
Sans Serif

Colors
f78f20
0455a3

Requirements
Must have
• My company name: TORVEL Maintenance Industrielle My phone: (450) -318-5947 My email: torvel.mnt@boitemel-exemple.com
Nice to have
• Integrate a representative logo of the mechanics (gears, mechanical parts)

```html
<!DOCTYPE html>
<html lang="fr">
<head>
<meta charset="utf-8">
<title>TORVEL Maintenance Industrielle – Cartes d'affaires</title>
<link rel="stylesheet" href="https://fonts.googleapis.com/css2?family=Montserrat:wght@400;800&display=swap">
<style>
  :root {
    --orange: #f78f20;
    --orange-light: #f8ab3f;
    --orange-deep: #ee7f14;
    --blue: #0455a3;
    --blue-deep: #0a3f9c;
    --blue-light: #2a70c2;
    --decor-blue: #5c86c8;
    --white: #ffffff;
    --backdrop: #ece8e2;
  }
  * { margin: 0; padding: 0; box-sizing: border-box; }
  html, body {
    width: 1200px;
    height: 1000px;
    overflow: hidden;
    background: var(--backdrop);
    font-family: "Montserrat", sans-serif;
  }
  .canvas {
    position: relative;
    width: 1200px;
    height: 1000px;
  }
  .card {
    position: absolute;
    left: 250px;
    width: 700px;
    height: 400px;
    overflow: hidden;
    box-shadow: 0 10px 30px rgba(0,0,0,0.18);
  }
  .card-front {
    top: 60px;
    background: linear-gradient(100deg, var(--orange-deep) 0%, var(--orange) 50%, var(--orange-light) 100%);
    display: flex;
    align-items: center;
    justify-content: center;
  }
  .card-back {
    top: 520px;
    background: linear-gradient(100deg, var(--blue-deep) 0%, var(--blue) 55%, var(--blue-light) 100%);
  }
  .brand {
    display: flex;
    align-items: center;
    gap: 16px;
  }
  .brand-dot {
    width: 58px;
    height: 58px;
    border-radius: 50%;
    flex: none;
  }
  .brand-name {
    font-weight: 800;
    line-height: 1;
  }
  .brand-name .name-main {
    display: block;
    font-size: 52px;
    letter-spacing: 1px;
  }
  .brand-name .name-sub {
    display: block;
    font-size: 17px;
    margin-top: 4px;
  }
  .card-front .brand-dot { background: var(--blue); }
  .card-front .brand-name { color: var(--blue); }
  .card-back .brand {
    position: absolute;
    left: 40px;
    top: 60px;
  }
  .card-back .brand-dot { width: 74px; height: 74px; background: var(--orange); }
  .card-back .brand-name { color: var(--orange); }
  .card-back .brand-name .name-main { font-size: 58px; }
  .card-back .brand-name .name-sub { font-size: 19px; }
  .gear-decor {
    position: absolute;
    right: 10px;
    top: 20px;
    width: 290px;
    height: 270px;
    border-radius: 50%;
    background: radial-gradient(circle at 55% 60%, rgba(120,160,220,0.55) 0%, rgba(92,134,200,0.35) 55%, rgba(92,134,200,0) 72%);
  }
  .contact {
    position: absolute;
    left: 40px;
    top: 250px;
    list-style: none;
    color: var(--white);
    font-size: 24px;
    font-weight: 400;
  }
  .contact li {
    display: flex;
    align-items: center;
    gap: 16px;
    height: 46px;
  }
  .contact svg { width: 26px; height: 26px; flex: none; }
  .band {
    position: absolute;
    left: 0;
    bottom: 0;
    width: 700px;
    height: 42px;
  }
</style>
</head>
<body>
<main class="canvas">

  <section class="card card-front" aria-label="Recto de la carte">
    <div class="brand">
      <span class="brand-dot"></span>
      <p class="brand-name">
        <span class="name-main">TORVEL</span>
        <span class="name-sub">Maintenance Industrielle</span>
      </p>
    </div>
  </section>

  <section class="card card-back" aria-label="Verso de la carte">
    <div class="gear-decor" role="img" aria-label="Engrenages décoratifs bleu pâle"></div>

    <div class="brand">
      <span class="brand-dot"></span>
      <p class="brand-name">
        <span class="name-main">TORVEL</span>
        <span class="name-sub">Maintenance Industrielle</span>
      </p>
    </div>

    <ul class="contact">
      <li>
        <svg viewBox="0 0 24 24" aria-hidden="true"><path fill="#f78f20" d="M6.6 10.8a15.1 15.1 0 0 0 6.6 6.6l2.2-2.2a1 1 0 0 1 1-.25 11.4 11.4 0 0 0 3.6.57 1 1 0 0 1 1 1V20a1 1 0 0 1-1 1A17 17 0 0 1 3 4a1 1 0 0 1 1-1h3.5a1 1 0 0 1 1 1c0 1.25.2 2.46.57 3.6a1 1 0 0 1-.25 1z"/></svg>
        <span>(450)-318-5947</span>
      </li>
      <li>
        <svg viewBox="0 0 24 24" aria-hidden="true"><rect x="2" y="5" width="20" height="14" fill="#f78f20"/><path d="M2.5 5.5 12 13l9.5-7.5" fill="none" stroke="#0455a3" stroke-width="1.6"/></svg>
        <span>torvel.mnt@boitemel-exemple.com</span>
      </li>
    </ul>

    <svg class="band" viewBox="0 0 700 42" aria-hidden="true">
      <polygon points="0,0 428,0 414,28 700,28 700,42 0,42" fill="#f78f20"/>
      <polygon points="440,0 700,0 700,28 426,28" fill="#ffffff"/>
    </svg>
  </section>

</main>
</body>
</html>
```